Letterhead  - Transportation
Simple
Kestrel Haulage LLC
4829 West 62nd Avenue Brooklyn, NY 11254
kestrelhaulagellc@mailbox-example.com
morvanfelsby morvanfelsby
I'm looking for a business letterhead not a business card
Please use concept #172 in your letterhead design,

```html
<!DOCTYPE html>
<html lang="en">
<head>
<meta charset="utf-8">
<title>Kestrel Haulage LLC – Letterhead</title>
<link href="https://fonts.googleapis.com/css2?family=PT+Sans:wght@400;700&display=swap" rel="stylesheet">
<style>
  :root {
    --backdrop: #000000;
    --paper: #ffffff;
    --navy: #0f3459;
    --orange: #f0872a;
    --mark-faint: #f2f2f2;
    --caption: #ffffff;
  }
  * { margin: 0; padding: 0; box-sizing: border-box; }
  html, body {
    width: 937px; height: 1200px; overflow: hidden;
    background: var(--backdrop);
    font-family: "PT Sans", sans-serif;
  }
  .board { position: relative; width: 937px; height: 1200px; }
  .letterhead {
    position: absolute; left: 203px; top: 250px;
    width: 523px; height: 676px;
    background: var(--paper); overflow: hidden;
  }
  .brand-name {
    position: absolute; left: 24px; top: 84px;
    font-size: 22px; font-weight: 700; color: var(--navy);
    white-space: nowrap; letter-spacing: 0.2px;
  }
  .contact {
    position: absolute; right: 36px; top: 36px;
    list-style: none; text-align: right;
    font-size: 11.5px; color: var(--navy);
  }
  .contact li {
    display: flex; justify-content: flex-end; align-items: center;
    height: 17.5px; gap: 6px;
  }
  .contact .icon { width: 18px; height: 14px; fill: var(--navy); flex: none; }
  .contact .icon-blank { width: 18px; flex: none; }
  .faint-mark {
    position: absolute; left: 0; right: 0; top: 330px;
    text-align: center; font-size: 40px; font-weight: 700;
    color: var(--mark-faint); white-space: nowrap;
  }
  .footer-swoosh { position: absolute; left: 0; top: 0; width: 523px; height: 676px; }
  .caption {
    position: absolute; left: 0; right: 0; top: 976px;
    text-align: center; color: var(--caption);
    font-size: 23px; font-weight: 400; letter-spacing: 0.3px;
  }
</style>
</head>
<body>
<div class="board">
  <section class="letterhead">
    <div class="brand-name">Kestrel Haulage LLC</div>

    <ul class="contact">
      <li>4829 West 62nd Avenue
        <svg class="icon" viewBox="0 0 18 14"><path d="M9 0 L18 7 H15.5 V14 H11 V9.5 H7 V14 H2.5 V7 H0 Z"/></svg>
      </li>
      <li>Brooklyn, NY 11254<span class="icon-blank"></span></li>
      <li>7185550143
        <svg class="icon" viewBox="0 0 18 14"><path d="M5.5 0 H12.5 V14 H5.5 Z M6.8 1.5 V11 H11.2 V1.5 Z"/></svg>
      </li>
      <li>7185550178
        <svg class="icon" viewBox="0 0 18 14"><path d="M4 0 H14 V4 H4 Z M1 5 H17 V11 H14 V9 H4 V11 H1 Z M5 10 H13 V14 H5 Z"/></svg>
      </li>
      <li>kestrelhaulagellc@mailbox-example.com
        <svg class="icon" viewBox="0 0 18 14"><path d="M0 2 H18 V12 H0 Z" /><path d="M0.5 2.5 L9 8 L17.5 2.5" stroke="#fff" stroke-width="1.2" fill="none"/></svg>
      </li>
    </ul>

    <div class="faint-mark">Kestrel Haulage LLC</div>

    <svg class="footer-swoosh" viewBox="0 0 523 676" aria-hidden="true">
      <path fill="var(--navy)" d="M0,588 C60,630 200,655 350,664 C430,668 490,660 523,651 C480,666 420,672 340,672 C200,670 60,660 0,629 Z"/>
      <path fill="var(--orange)" d="M0,640 C40,655 100,664 160,667 C100,669 40,667 0,660 Z"/>
    </svg>
  </section>

  <div class="caption">LETTER HEAD</div>
</div>
</body>
</html>
```